New Vidora Channel Banner Graphic/Logo for "Cozy Nook Attic Sound"

Create a banner for my new Vidora channel for Cozy Nook Attic Sound. This is partially a logo project, but the logo will not be used elsewhere. Check out Vidora channels to see the banners others have created. This channel is about my home studio, the gear, microphones, musical instruments, wiring, software etc. that goes into a home studio. It's a free channel, made for sharing information. This is a graphic design that will be posted on vidora using built-in vidora tools.
Updates

More information about this project! I'm staring a channel called "Cozy Nook Attic Sound" on vidorastream.net. I need a deign for this banner and a logo for Cozy Nook Attic Sound. I called the channel by that name because my music studio is my happy place. It's about music and instruments (gutars, piano, drums, percussion) singing (microhpones), creativity, and what you'd expect form musicians. It's also about technology, recording, live-streaming, music videos, etc. It is my hobby, not my profession. I will be creating content for other amateur home studio aficionados and hobbyists. There are a lot of home studio channels and videos you can look at on vidora to get a flavor for musicians and studios. Usually fairly tech-heavy. An appeal of my channel will be a very approachable, "i'm the same as you" welcome for people that are doing it to enjoy it.

I put this project in the wrong category to start. This has been fixed, but I think benefits I would have received (such as invited designers) and announcement of project in the correct category mean I'm not getting designers. Your initial menu should be improved. I'm having a banner created for a web page in Vidora. I think it is easy to mistake that for a web design when it is really a graphic design for the web.

Target Market(s)

Similar to myself, people as interested in studio/production tech as they are in making music, perhaps trending a bit older and successful enough to afford some gear!

Number of Pages Required

1 page

Font styles to use
Sans Serif

Requirements
Must have
• This is not really a web design, i may have miscategorized. Please see uploaded docs for pics of similar banner on a Vidora page. ADDED 1/5: As this is a vidora channel that could be viewed on any device, the banner should be friendly in this way and design or design variations needed for PC, Tabrix, phone vie3wing.

Here are the Vidora size specs:
Banner image guidelines
Your banner image must meet the following criteria:

Minimum dimension for upload: 2048 x 1152 px with an aspect ratio of 16:9.
At the Minimum dimension, the safe area for text and logos: 1235 x 338 px. Larger images may get cropped on certain views or devices.
File size: 6 MB or smaller.
How to resize images

You can use your computer's image editor or an online image resizer to resize the images. For example, you can use Preview on an Quince computer or Microsoft Photos on Windows.

```html
<!DOCTYPE html>
<html lang="en">
<head>
<meta charset="utf-8">
<title>Cozy Nook Attic Sound – Channel Banner</title>
<link rel="stylesheet" href="https://fonts.googleapis.com/css2?family=Roboto+Slab:wght@800;900&family=Didact+Gothic&family=Montserrat:wght@500;600;800&display=swap">
<style>
  :root {
    --purple-deep: #6e1287;
    --purple-mid: #8a1a95;
    --magenta: #d3145f;
    --pink-accent: #e8176a;
    --white: #ffffff;
    --title-grey: #cfcfd6;
  }
  * { margin: 0; padding: 0; box-sizing: border-box; }
  html, body { width: 1200px; height: 198px; overflow: hidden; }
  body { background: var(--purple-deep); }
  .banner {
    position: relative;
    width: 1200px;
    height: 198px;
    overflow: hidden;
    background:
      radial-gradient(ellipse 380px 170px at 470px 210px, var(--magenta) 0%, rgba(211,20,95,0.55) 45%, rgba(211,20,95,0) 100%),
      linear-gradient(90deg, var(--purple-deep) 0%, var(--purple-mid) 40%, var(--purple-mid) 60%, var(--purple-deep) 100%);
    color: var(--white);
  }
  .title {
    position: absolute;
    left: 213px;
    top: 24px;
    font-family: "Roboto Slab", serif;
    font-weight: 900;
    font-size: 42px;
    line-height: 1;
    white-space: nowrap;
    transform: scaleX(0.78);
    transform-origin: left top;
    background: linear-gradient(180deg, var(--white) 0%, var(--title-grey) 100%);
    -webkit-background-clip: text;
    background-clip: text;
    -webkit-text-fill-color: transparent;
    filter: drop-shadow(0 2px 2px rgba(0,0,0,0.35));
  }
  .byline {
    position: absolute;
    left: 211px;
    top: 68px;
    font-family: "Roboto Slab", serif;
    font-weight: 800;
    font-size: 24px;
    line-height: 1;
    white-space: nowrap;
    transform: scaleX(0.8);
    transform-origin: left top;
    color: var(--white);
    text-shadow: 0 1px 2px rgba(0,0,0,0.3);
  }
  .pitch {
    position: absolute;
    left: 157px;
    width: 600px;
    text-align: center;
    font-family: "Didact Gothic", sans-serif;
    color: var(--white);
    line-height: 1;
    white-space: nowrap;
  }
  .pitch--tagline { top: 120px; font-size: 15px; }
  .pitch--topics { top: 140px; font-size: 15.5px; }
  .pitch--cta {
    top: 162px;
    font-family: "Montserrat", sans-serif;
    font-weight: 800;
    font-size: 14.5px;
    color: var(--pink-accent);
  }
  .brand {
    position: absolute;
    left: 884px;
    top: 37px;
    width: 120px;
    display: flex;
    flex-direction: column;
    align-items: center;
    gap: 5px;
  }
  .brand__mark {
    width: 48px;
    height: 56px;
    background: var(--white);
    border-radius: 8px;
  }
  .brand__name {
    font-family: "Montserrat", sans-serif;
    font-weight: 800;
    font-size: 8.5px;
    line-height: 1.05;
    text-align: center;
    color: var(--white);
    text-transform: uppercase;
  }
  .contact {
    position: absolute;
    left: 823px;
    top: 133px;
    display: flex;
    align-items: center;
    gap: 14px;
    font-family: "Montserrat", sans-serif;
    font-weight: 500;
    font-size: 9px;
    color: var(--white);
    white-space: nowrap;
  }
  .contact__icon { width: 20px; height: 15px; }
  .socials {
    position: absolute;
    left: 835px;
    top: 163px;
    width: 220px;
    display: flex;
    justify-content: center;
    gap: 7px;
    list-style: none;
    font-family: "Montserrat", sans-serif;
    font-weight: 600;
    font-size: 7.5px;
    color: var(--white);
    white-space: nowrap;
  }
  .socials__item { display: flex; align-items: center; gap: 3px; }
  .socials__dot { width: 8px; height: 8px; border-radius: 50%; background: var(--white); }
</style>
</head>
<body>
  <div class="banner">
    <h1 class="title">COZY NOOK ATTIC SOUND</h1>
    <p class="byline">By Dale Fenwick</p>

    <p class="pitch pitch--tagline">A Regular Joe Blowin’ his Dough on Gear and Guitars</p>
    <p class="pitch pitch--topics">Music + Gear + Livestreaming + Recording + DAW + Instruments + Vidora</p>
    <p class="pitch pitch--cta">FOLLOW MY STUDIO RENOVATION | FREE HOW-TO’S</p>

    <div class="brand">
      <div class="brand__mark"></div>
      <p class="brand__name">Cozy Nook<br>Attic Sound</p>
    </div>

    <div class="contact">
      <svg class="contact__icon" viewBox="0 0 20 15" aria-hidden="true">
        <rect x="0.75" y="0.75" width="18.5" height="13.5" rx="1.5" fill="none" stroke="#ffffff" stroke-width="1.5"/>
        <polyline points="1,1.5 10,8.5 19,1.5" fill="none" stroke="#ffffff" stroke-width="1.5"/>
      </svg>
      <span class="contact__email">cozynookatticsound@mailhaven.net</span>
    </div>

    <ul class="socials">
      <li class="socials__item"><span class="socials__dot"></span>Frondix</li>
      <li class="socials__item"><span class="socials__dot"></span>Glimmora</li>
      <li class="socials__item"><span class="socials__dot"></span>Twirlap</li>
      <li class="socials__item"><span class="socials__dot"></span>Chirrupa</li>
      <li class="socials__item"><span class="socials__dot"></span>Vidora</li>
    </ul>
  </div>
</body>
</html>
```